First of a series of workplace posters- our values statement

To produce a high quality poster of our values, we would like one in a3 and one in a4 both full colour
By utilising the supplied text , the intent is to produce a really striking poster for all our work places, which set out our company values. we are looking for really strong graphical elements which support the message visually . This will be the first of a series of posters, so we are looking to establish at stylistic theme for all with this one. for more on our business,

Target Market(s)

Internal and external audiences, our clients are all tier one companies

Requirements
Must have
• contemporary design rather than conservative, visually striking
• Must be clearly readable from a reasonable distance
Nice to have
• would be nice to tie in to the blue and greens of our logo in similar fashion to our website. www.qrtbuildwise.com
Should not have
• Difficult to read fonts,

```html
<!DOCTYPE html>
<html lang="en">
<head>
<meta charset="utf-8">
<title>Our Values 01 – People</title>
<link href="https://fonts.googleapis.com/css2?family=Raleway:wght@500;800;900&display=swap" rel="stylesheet">
<style>
  :root {
    --teal: #24595a;
    --teal-deep: #123637;
    --teal-shadow: #0b2223;
    --white: #ffffff;
  }
  * { margin: 0; padding: 0; box-sizing: border-box; }
  html, body { width: 849px; height: 1200px; overflow: hidden; background: var(--teal); }
  .poster {
    position: relative;
    width: 849px;
    height: 1200px;
    overflow: hidden;
    font-family: "Raleway", Arial, sans-serif;
    color: var(--white);
    font-variant-numeric: lining-nums;
  }
  .poster__photo {
    position: absolute;
    inset: 0;
    background:
      radial-gradient(ellipse 60% 45% at 18% 35%, rgba(11,34,35,0.85), rgba(11,34,35,0) 70%),
      radial-gradient(ellipse 70% 35% at 45% 95%, rgba(11,34,35,0.9), rgba(11,34,35,0) 70%),
      linear-gradient(90deg, var(--teal-deep) 0%, #1a4546 38%, var(--teal) 62%, var(--teal) 100%);
  }
  .value-number {
    position: absolute;
    left: 104px;
    top: 98px;
    font-size: 122px;
    font-weight: 900;
    line-height: 1;
    letter-spacing: -2px;
  }
  .headline {
    position: absolute;
    left: 103px;
    top: 482px;
    font-size: 72px;
    font-weight: 800;
    line-height: 80px;
    letter-spacing: -1px;
  }
  .pledge {
    position: absolute;
    width: 189px;
    border-top: 2.5px solid var(--white);
    padding-top: 20px;
    font-size: 19.5px;
    font-weight: 500;
    line-height: 23.5px;
  }
  .pledge--safe       { left: 103px; top: 808px; }
  .pledge--inclusion  { left: 330px; top: 808px; }
  .pledge--support    { left: 557px; top: 808px; }
  .pledge--careers    { left: 106px; top: 1007px; }
  .pledge--recognise  { left: 330px; top: 983px; padding-top: 25px; }
  .pledge--balance    { left: 558px; top: 983px; padding-top: 20px; }
</style>
</head>
<body>
<main class="poster">
  <div class="poster__photo" role="img" aria-label="Teal-toned photograph of two business people in suits shaking hands across a desk"></div>

  <div class="value-number">01</div>

  <h1 class="headline">We value our<br>people above<br>everything else.</h1>

  <p class="pledge pledge--safe">Providing safe, positive, enjoyable workplaces where everyone feels valued and respected.</p>
  <p class="pledge pledge--inclusion">Encouraging inclusion, participation and&nbsp;collaboration.</p>
  <p class="pledge pledge--support">Supporting our people through tough times.</p>
  <p class="pledge pledge--careers">Providing careers, not jobs, we grow together.</p>
  <p class="pledge pledge--recognise">Recognising and rewarding contribution and excellence.</p>
  <p class="pledge pledge--balance">Fostering healthy work life&nbsp;balance.</p>
</main>
</body>
</html>
```